High performance dog care

We need a high performance care label for dog show specialists;
The relationship with the canine world can be discreet; we prefer that there are no pictures of dogs
The label will be affixed to a round bottle (see photo);
This tag measures 150mm wide by 170mm high; the visible part for the front graphics is 45mm wide by 170mm high
These products are intended for competitors in the dog grooming and breeding sectors.
The addition of foil (gold or silver) is quite possible

Target Market(s)

Professional dog shows

Industry/Entity Type

Cosmetics

Requirements
Must have
• An elegant and technical look
The word "Vell" as a title
Subtitle: for example: Argan
Description: nourishing treatment (in English and French)
In text or symbol: no para ben, no silicone, no sulfate, no dyes
Nice to have
• There are currently 4 different products which should be distinct from each other while together forming a homogeneity of the range
- nourishing treatment: argan, jojoba oil, almond oil
- volumizing treatment: keratin and hyaluronic acid
- smoothing treatment: silk protein from JApon
- restructuring treatment: avocado and macadamia oil
-
Should not have
• Humorous cartoons

```html
<!DOCTYPE html>
<html lang="en">
<head>
<meta charset="utf-8">
<title>Vell – Care Range Labels</title>
<link href="https://fonts.googleapis.com/css2?family=Didact+Gothic&display=swap" rel="stylesheet">
<style>
  :root {
    --page-bg: #f1f2f2;
    --label-bg: #ffffff;
    --grey-text: #6d6e70;
    --badge-grey: #7a7b7d;

    --argan-dark: #c98a4a;
    --argan-light: #fde3c3;
    --argan-band: #f9c98a;
    --argan-head: #d08b3e;

    --keratin-dark: #3a86cc;
    --keratin-light: #bcdcf5;
    --keratin-band: #74b1e4;
    --keratin-head: #2f86cf;

    --silk-dark: #e05a4a;
    --silk-light: #f5c6be;
    --silk-band: #f08a7c;
    --silk-head: #e2453a;

    --avocado-dark: #4e9e2e;
    --avocado-light: #aee384;
    --avocado-band: #74c45a;
    --avocado-head: #3f9a22;
  }
  * { margin: 0; padding: 0; box-sizing: border-box; }
  html, body {
    width: 1200px; height: 783px; overflow: hidden;
    background: var(--page-bg);
    font-family: "Didact Gothic", sans-serif;
  }
  .range {
    display: flex; gap: 40px;
    padding: 41px 40px;
  }
  .label {
    width: 250px; height: 700px;
    background: var(--label-bg);
    box-shadow: 0 1px 4px rgba(0,0,0,0.08);
  }
  .label svg { display: block; }
  .label text { font-family: "Didact Gothic", sans-serif; }

  .argan   { --dark: var(--argan-dark);   --light: var(--argan-light);   --band: var(--argan-band);   --head: var(--argan-head); }
  .keratin { --dark: var(--keratin-dark); --light: var(--keratin-light); --band: var(--keratin-band); --head: var(--keratin-head); }
  .silk    { --dark: var(--silk-dark);    --light: var(--silk-light);    --band: var(--silk-band);    --head: var(--silk-head); }
  .avocado { --dark: var(--avocado-dark); --light: var(--avocado-light); --band: var(--avocado-band); --head: var(--avocado-head); }

  .bar-light { fill: var(--light); }
  .bar-dark { fill: var(--dark); }
  .bar-band { fill: var(--band); }
  .ingredients { fill: var(--dark); font-size: 20px; }
  .brand-name { fill: #ffffff; font-size: 58px; letter-spacing: 1px; }
  .brand-dot { fill: var(--light); stroke: var(--dark); stroke-width: 3; }
  .title { fill: var(--head); font-size: 26px; }
  .title-rule { stroke: var(--head); stroke-width: 2.5; }
  .subtitle { fill: var(--grey-text); font-size: 21px; }
  .badge-ring { fill: none; stroke: var(--badge-grey); stroke-width: 1.6; }
  .badge-text { fill: var(--badge-grey); font-size: 8.5px; text-anchor: middle; }
  .badge-free { fill: var(--badge-grey); font-size: 11px; font-weight: bold; text-anchor: middle; }
</style>
</head>
<body>
<main class="range">

  <!-- Nourishing: argan -->
  <section class="label argan">
    <svg width="250" height="700" viewBox="0 0 250 700">
      <path class="bar-light" d="M32 118 a29 29 0 0 1 58 0 V434 H32 Z"/>
      <rect class="bar-dark" x="32" y="434" width="58" height="150"/>
      <rect class="bar-band" x="32" y="584" width="58" height="28"/>
      <text class="ingredients" transform="translate(70 420) rotate(-90)">Argan | Jojoba Oil | Almond Oil</text>
      <text class="brand-name" transform="translate(84 572) rotate(-90)">Vell</text>
      <circle class="brand-dot" cx="112" cy="610" r="22"/>
      <text class="title" x="96" y="140">Nourishing</text>
      <text class="title" x="96" y="167">Treatment</text>
      <line class="title-rule" x1="96" y1="212" x2="210" y2="212"/>
      <text class="subtitle" x="96" y="236">Traitement</text>
      <text class="subtitle" x="96" y="260">Nourrissant</text>
      <g transform="translate(178 358)"><circle class="badge-ring" r="24"/><text class="badge-text" y="0">PARABEN</text><text class="badge-free" y="12">FREE</text></g>
      <g transform="translate(178 413)"><circle class="badge-ring" r="24"/><text class="badge-text" y="0">SILICONE</text><text class="badge-free" y="12">FREE</text></g>
      <g transform="translate(178 468)"><circle class="badge-ring" r="24"/><text class="badge-text" y="0">SULFATE</text><text class="badge-free" y="12">FREE</text></g>
      <g transform="translate(178 523)"><circle class="badge-ring" r="24"/><text class="badge-text" y="0">DYES</text><text class="badge-free" y="12">FREE</text></g>
    </svg>
  </section>

  <!-- Volumizing: keratin -->
  <section class="label keratin">
    <svg width="250" height="700" viewBox="0 0 250 700">
      <path class="bar-light" d="M32 118 a29 29 0 0 1 58 0 V434 H32 Z"/>
      <rect class="bar-dark" x="32" y="434" width="58" height="150"/>
      <rect class="bar-band" x="32" y="584" width="58" height="28"/>
      <text class="ingredients" transform="translate(70 420) rotate(-90)">Keratin | Hyaluronic Acid</text>
      <text class="brand-name" transform="translate(84 572) rotate(-90)">Vell</text>
      <circle class="brand-dot" cx="112" cy="610" r="22"/>
      <text class="title" x="96" y="140">Nourishing</text>
      <text class="title" x="96" y="167">Treatment</text>
      <line class="title-rule" x1="96" y1="212" x2="210" y2="212"/>
      <text class="subtitle" x="96" y="236">Traitement</text>
      <text class="subtitle" x="96" y="260">Nourrissant</text>
      <g transform="translate(178 358)"><circle class="badge-ring" r="24"/><text class="badge-text" y="0">PARABEN</text><text class="badge-free" y="12">FREE</text></g>
      <g transform="translate(178 413)"><circle class="badge-ring" r="24"/><text class="badge-text" y="0">SILICONE</text><text class="badge-free" y="12">FREE</text></g>
      <g transform="translate(178 468)"><circle class="badge-ring" r="24"/><text class="badge-text" y="0">SULFATE</text><text class="badge-free" y="12">FREE</text></g>
      <g transform="translate(178 523)"><circle class="badge-ring" r="24"/><text class="badge-text" y="0">DYES</text><text class="badge-free" y="12">FREE</text></g>
    </svg>
  </section>

  <!-- Smoothing: silk protein -->
  <section class="label silk">
    <svg width="250" height="700" viewBox="0 0 250 700">
      <path class="bar-light" d="M32 118 a29 29 0 0 1 58 0 V434 H32 Z"/>
      <rect class="bar-dark" x="32" y="434" width="58" height="150"/>
      <rect class="bar-band" x="32" y="584" width="58" height="28"/>
      <text class="ingredients" transform="translate(70 420) rotate(-90)">Silk Protein from Japan</text>
      <text class="brand-name" transform="translate(84 572) rotate(-90)">Vell</text>
      <circle class="brand-dot" cx="112" cy="610" r="22"/>
      <text class="title" x="96" y="140">Nourishing</text>
      <text class="title" x="96" y="167">Treatment</text>
      <line class="title-rule" x1="96" y1="212" x2="210" y2="212"/>
      <text class="subtitle" x="96" y="236">Traitement</text>
      <text class="subtitle" x="96" y="260">Nourrissant</text>
      <g transform="translate(178 358)"><circle class="badge-ring" r="24"/><text class="badge-text" y="0">PARABEN</text><text class="badge-free" y="12">FREE</text></g>
      <g transform="translate(178 413)"><circle class="badge-ring" r="24"/><text class="badge-text" y="0">SILICONE</text><text class="badge-free" y="12">FREE</text></g>
      <g transform="translate(178 468)"><circle class="badge-ring" r="24"/><text class="badge-text" y="0">SULFATE</text><text class="badge-free" y="12">FREE</text></g>
      <g transform="translate(178 523)"><circle class="badge-ring" r="24"/><text class="badge-text" y="0">DYES</text><text class="badge-free" y="12">FREE</text></g>
    </svg>
  </section>

  <!-- Restructuring: avocado -->
  <section class="label avocado">
    <svg width="250" height="700" viewBox="0 0 250 700">
      <path class="bar-light" d="M32 118 a29 29 0 0 1 58 0 V434 H32 Z"/>
      <rect class="bar-dark" x="32" y="434" width="58" height="150"/>
      <rect class="bar-band" x="32" y="584" width="58" height="28"/>
      <text class="ingredients" transform="translate(70 420) rotate(-90)">Avocado &amp; Macadamian Oil</text>
      <text class="brand-name" transform="translate(84 572) rotate(-90)">Vell</text>
      <circle class="brand-dot" cx="112" cy="610" r="22"/>
      <text class="title" x="96" y="140">Nourishing</text>
      <text class="title" x="96" y="167">Treatment</text>
      <line class="title-rule" x1="96" y1="212" x2="210" y2="212"/>
      <text class="subtitle" x="96" y="236">Traitement</text>
      <text class="subtitle" x="96" y="260">Nourrissant</text>
      <g transform="translate(178 358)"><circle class="badge-ring" r="24"/><text class="badge-text" y="0">PARABEN</text><text class="badge-free" y="12">FREE</text></g>
      <g transform="translate(178 413)"><circle class="badge-ring" r="24"/><text class="badge-text" y="0">SILICONE</text><text class="badge-free" y="12">FREE</text></g>
      <g transform="translate(178 468)"><circle class="badge-ring" r="24"/><text class="badge-text" y="0">SULFATE</text><text class="badge-free" y="12">FREE</text></g>
      <g transform="translate(178 523)"><circle class="badge-ring" r="24"/><text class="badge-text" y="0">DYES</text><text class="badge-free" y="12">FREE</text></g>
    </svg>
  </section>

</main>
</body>
</html>
```